I am a surgeon that operates on gynaecological cancer. Wish a design and logo for letter head.

Design should include my name: Dr. Kiran Mudaly, qualifications: FTELSWOB, CGO. and state that I am a Gynaecological Oncologist and Advanced Laparoscopic Surgeon.
As for a logo. As all cancer is related to DNA, I think that that double helix could be used to symbolise a female shape, exaggerating the abdomen to suggest a mass.

Reason: Extended to view changes I have asked for.

```html
<!DOCTYPE html>
<html lang="en">
<head>
<meta charset="utf-8">
<title>Dr. Kiran Mudaly – Letterhead</title>
<link rel="stylesheet" href="https://fonts.googleapis.com/css2?family=PT+Sans&family=Share+Tech+Mono&display=swap">
<style>
  :root {
    --header-grey: #5d5e60;
    --ink: #0a0a0a;
    --rule: #000000;
    --paper: #ffffff;
  }
  html, body {
    margin: 0;
    padding: 0;
    width: 848px;
    height: 1200px;
    overflow: hidden;
    background: var(--paper);
  }
  .letterhead {
    position: relative;
    width: 848px;
    height: 1200px;
    background: var(--paper);
    font-family: "PT Sans", sans-serif;
    color: var(--ink);
  }
  .masthead {
    position: absolute;
    left: 0;
    top: 0;
    width: 848px;
    height: 186px;
    background: var(--header-grey);
  }
  .brand-mark {
    position: absolute;
    left: 113px;
    top: 37px;
    width: 70px;
    height: 134px;
    display: flex;
    align-items: center;
    justify-content: center;
    font-family: "PT Sans", sans-serif;
    font-size: 15px;
    color: var(--ink);
  }
  .doctor-name {
    position: absolute;
    left: 209px;
    top: 34px;
    margin: 0;
    font-family: "Share Tech Mono", monospace;
    font-weight: 400;
    font-size: 28px;
    letter-spacing: 2.1px;
    line-height: 1;
    white-space: nowrap;
  }
  .qualifications {
    position: absolute;
    left: 508px;
    top: 44px;
    font-size: 16px;
    line-height: 1;
    white-space: nowrap;
  }
  .title-rule {
    position: absolute;
    left: 204px;
    top: 75px;
    width: 551px;
    height: 4px;
    background: var(--rule);
  }
  .specialty {
    position: absolute;
    left: 207px;
    top: 86px;
    margin: 0;
    font-size: 17px;
    font-weight: 400;
    line-height: 1;
    white-space: nowrap;
  }
  .contact-block {
    position: absolute;
    top: 120px;
    margin: 0;
    font-style: normal;
    font-size: 13px;
    line-height: 17px;
    white-space: nowrap;
  }
  .contact-block--address { left: 207px; }
  .contact-block--numbers { left: 508px; }
</style>
</head>
<body>
  <div class="letterhead">
    <header class="masthead">
      <div class="brand-mark">Mudaly</div>
      <h1 class="doctor-name">Dr. Kiran Mudaly</h1>
      <span class="qualifications">FTELSWOB, CGO</span>
      <div class="title-rule"></div>
      <h2 class="specialty">Gynaecological Oncologist and Advanced Laparoscopic Surgeon</h2>
      <address class="contact-block contact-block--address">
        12 Alder Street<br>
        Lakeside Heights<br>
        4712
      </address>
      <address class="contact-block contact-block--numbers">
        T: 000 000-0000<br>
        F: 000 000-000<br>
        E: drkmudaly@kiranmudaly.com
      </address>
    </header>
  </div>
</body>
</html>
```